Looking for a professional, clean and crisp business card

I am in the underground utilities industry and am just looking for a really impressive business card. I would like our card to be white with our symbol crisp and clear with it protruding. I also have a business partner that will require his name and info on the card once the design is set. I would like to have our website info on the card which is;
http://harbortrenchco.example/

Contact Information for Business Card

Website, contact name, number and email

```html
<!DOCTYPE html>
<html lang="en">
<head>
<meta charset="utf-8">
<title>Harbor Trench Co — Business Card</title>
<link href="https://fonts.googleapis.com/css2?family=Arimo:wght@400;700&display=swap" rel="stylesheet">
<style>
  :root {
    --stage: #3a3430;
    --card-dark: #131313;
    --card-light: #ffffff;
    --ink: #3d3d3d;
    --ink-soft: #555555;
    --accent-blue: #2f5bab;
    --accent-red: #e3262b;
    --mark-light: #ffffff;
    --mark-dark: #1b1b1b;
  }
  * { box-sizing: border-box; margin: 0; padding: 0; }
  html, body { width: 1200px; height: 716px; overflow: hidden; }
  body {
    background: var(--stage);
    font-family: "Arimo", Arial, sans-serif;
    position: relative;
  }
  .card {
    position: absolute;
    top: 204px;
    width: 540px;
    height: 309px;
    box-shadow: 0 10px 24px rgba(0,0,0,0.35);
  }
  .card--front { left: 40px; background: var(--card-dark); display: flex; align-items: center; justify-content: center; }
  .card--back { left: 620px; background: var(--card-light); }

  .wordmark { display: flex; align-items: center; gap: 12px; font-weight: 700; }
  .wordmark__dot { width: 22px; height: 22px; border-radius: 50%; }
  .card--front .wordmark { color: var(--mark-light); font-size: 30px; }
  .card--front .wordmark__dot { background: var(--mark-light); }

  .person { position: absolute; left: 52px; top: 38px; }
  .person__name { color: var(--accent-blue); font-weight: 700; font-size: 22px; }
  .person__title { color: var(--ink-soft); font-size: 13px; margin-top: 2px; }

  .divider { position: absolute; left: 52px; right: 52px; top: 128px; height: 1px; background: var(--accent-red); }

  .contact { position: absolute; left: 52px; top: 146px; list-style: none; }
  .contact__item { display: flex; align-items: center; gap: 8px; font-size: 13px; color: var(--ink); line-height: 19px; }
  .contact__icon { width: 11px; height: 11px; fill: var(--accent-blue); flex: none; }

  .card--back .wordmark { position: absolute; right: 40px; top: 80px; color: var(--mark-dark); font-size: 19px; }
  .card--back .wordmark__dot { background: var(--mark-dark); width: 16px; height: 16px; }

  .address { position: absolute; right: 44px; bottom: 30px; text-align: right; font-size: 14px; line-height: 19px; color: var(--ink); }
</style>
</head>
<body>
  <section class="card card--front" aria-label="Card front">
    <div class="wordmark"><span class="wordmark__dot"></span><span>Harbor Trench Co</span></div>
  </section>

  <section class="card card--back" aria-label="Card back">
    <div class="person">
      <p class="person__name">Dale Morrow</p>
      <p class="person__title">Owner/CEO</p>
    </div>

    <div class="wordmark"><span class="wordmark__dot"></span><span>Harbor Trench Co</span></div>

    <div class="divider"></div>

    <ul class="contact">
      <li class="contact__item">
        <svg class="contact__icon" viewBox="0 0 12 12"><path d="M2.5 0.5 4.5 3 3.5 4.5Q5 7.5 7.5 8.5L9 7.5 11.5 9.5 10 11.5Q5.5 11 2 6.5 0.5 3.5 2.5 0.5Z"/></svg>
        <span>555-014-2286</span>
      </li>
      <li class="contact__item">
        <svg class="contact__icon" viewBox="0 0 12 12"><path d="M3 0h6a1 1 0 0 1 1 1v10a1 1 0 0 1-1 1H3a1 1 0 0 1-1-1V1a1 1 0 0 1 1-1Zm0.5 1.5v8h5v-8Z"/></svg>
        <span>555-018-7730</span>
      </li>
      <li class="contact__item">
        <svg class="contact__icon" viewBox="0 0 12 12"><path d="M0 2h12v8H0Zm1 1 5 4 5-4Z"/></svg>
        <span>info@harbortrenchco.example</span>
      </li>
      <li class="contact__item">
        <svg class="contact__icon" viewBox="0 0 12 12"><circle cx="6" cy="6" r="5.5"/></svg>
        <span>www.harbortrenchco.example</span>
      </li>
    </ul>

    <address class="address" style="font-style:normal">
      1480 W Alder Road<br>
      Birch Hollow County<br>
      Region 4107
    </address>
  </section>
</body>
</html>
```